Drag Show Flyer

We are holding a Drag Show, we are looking for something fun and exciting, over the top is a must.

Show Date: Saturday September 2nd 2017
Venue: Pelican Row Cafe Bunbury
Doors open 7pm
Tickets: $50 per person, includes glass of sparkling on arrival and canapes
Tickets available at the Venue or from ticketloom.com.au

Target Market(s)

Female, Hens Party, LBGT

Industry/Entity Type

Entertainment

Colors

Designer to choose colors to be used in the design.

Requirements
Must have
• Show Date: Saturday September 2nd 2017
• Venue: Pelican Row Cafe Bunbury
• Doors open 7pm
• Tickets: $50 per person, includes glass of sparkling on arrival and canapes
• Tickets available at the Venue or from ticketloom.com.au

```html
<!DOCTYPE html>
<html lang="en">
<head>
<meta charset="utf-8">
<title>Cocktails &amp; Queens – Drag Show Flyer</title>
<link rel="stylesheet" href="https://fonts.googleapis.com/css2?family=Montserrat:ital,wght@0,500;0,700;0,800;0,900;1,800;1,900&family=Great+Vibes&display=swap">
<style>
  :root {
    --magenta-deep: #8a0a63;
    --magenta: #c4127f;
    --pink-hot: #e0229a;
    --pink-light: #f25cb8;
    --yellow: #ffe81a;
    --white: #ffffff;
    --black: #0b0b0b;
    --grey: #bdbdbd;
  }
  * { box-sizing: border-box; margin: 0; padding: 0; }
  html, body { width: 849px; height: 1200px; overflow: hidden; }
  body { font-family: "Montserrat", Arial, sans-serif; background: var(--black); }

  .flyer {
    position: relative;
    width: 849px;
    height: 1200px;
    overflow: hidden;
    background: radial-gradient(ellipse at 60% 40%, var(--pink-hot) 0%, var(--magenta) 45%, var(--magenta-deep) 100%);
  }

  .performer-photo {
    position: absolute;
    left: 0; top: 0;
    width: 470px; height: 1030px;
    background: linear-gradient(160deg, #f08ac8 0%, #e35aa8 25%, #f6b23a 55%, #e8a020 70%, #b01a78 100%);
    border-bottom-right-radius: 40px;
  }

  .crown-mark {
    position: absolute;
    left: 600px; top: 100px;
    width: 90px; height: 42px;
    background: var(--white);
    opacity: .9;
    border-radius: 6px;
  }

  .title { position: absolute; left: 450px; width: 390px; text-align: center; color: var(--white); white-space: nowrap; }
  .title-top { top: 168px; font-weight: 900; font-size: 38px; letter-spacing: 1px; }
  .title-script { top: 200px; font-family: "Great Vibes", cursive; font-size: 140px; line-height: 1.05; text-shadow: 0 4px 12px rgba(0,0,0,.35); }

  .tagline {
    position: absolute; left: 470px; top: 412px; width: 370px;
    color: var(--yellow); font-weight: 900; font-style: italic; white-space: nowrap;
    font-size: 22px; line-height: 1.2; text-align: center; transform: rotate(-6deg);
  }

  .show-date {
    position: absolute; left: 460px; top: 500px; width: 380px;
    text-align: center; color: var(--white); font-weight: 900; line-height: 1.08; white-space: nowrap;
  }
  .show-date .day { font-size: 56px; }
  .show-date .date { font-size: 50px; }

  .show-time {
    position: absolute; left: 460px; top: 640px; width: 380px;
    text-align: center; color: var(--yellow); font-weight: 800; font-size: 26px; white-space: nowrap;
  }

  .ticket-box {
    position: absolute; left: 475px; top: 700px; width: 355px; height: 125px;
    background: var(--pink-light);
    border: 3px dashed var(--white);
    border-radius: 14px;
    display: flex; align-items: center; gap: 12px; padding: 0 14px;
  }
  .ticket-box svg { flex: 0 0 54px; }
  .ticket-box p { color: var(--white); font-weight: 800; font-size: 14px; line-height: 1.35; text-transform: uppercase; }
  .ticket-box .hl { color: var(--yellow); }

  .presented {
    position: absolute; left: 35px; top: 845px;
    color: var(--white); font-weight: 800; font-size: 15px; line-height: 1.2; text-transform: uppercase;
  }
  .partner-badges { position: absolute; left: 35px; top: 895px; display: flex; gap: 16px; }
  .partner-badge { width: 62px; height: 62px; border-radius: 50%; background: var(--white); }

  .footer-band {
    position: absolute; left: 0; top: 1030px; width: 849px; height: 170px;
    background: var(--black);
  }
  .venue { position: absolute; left: 45px; top: 38px; color: var(--white); }
  .venue-name { display: flex; align-items: center; gap: 10px; font-weight: 800; font-size: 28px; }
  .venue-name .dot { width: 16px; height: 16px; border-radius: 50%; background: var(--white); }
  .venue-address { margin-top: 16px; font-weight: 500; font-size: 14px; color: var(--grey); text-transform: uppercase; line-height: 1.35; }

  .booking { position: absolute; left: 390px; top: 34px; width: 430px; text-align: right; text-transform: uppercase; white-space: nowrap; }
  .booking .lead { color: var(--white); font-weight: 800; font-size: 18px; }
  .booking .web { color: var(--yellow); font-weight: 900; font-size: 27px; line-height: 1.35; }
  .booking .phone { color: var(--yellow); font-weight: 900; font-size: 27px; line-height: 1.2; }
</style>
</head>
<body>
<main class="flyer">
  <div class="performer-photo" role="img" aria-label="Photo of a drag queen in a pink flower headpiece and yellow feather boa"></div>

  <div class="crown-mark" role="img" aria-label="Small crown ornament"></div>

  <h1>
    <span class="title title-top">COCKTAILS &amp;</span>
    <span class="title title-script">Queens</span>
  </h1>

  <p class="tagline">A NIGHT OF DRAG SHOWS<br>&amp; OUTRAGEOUS FUN!</p>

  <p class="show-date"><span class="day">SATURDAY</span><br><span class="date">SEPT 2, 2017</span></p>
  <p class="show-time">FROM 7PM TILL LATE!</p>

  <div class="ticket-box">
    <svg width="54" height="54" viewBox="0 0 58 58" aria-hidden="true">
      <circle cx="29" cy="29" r="27" fill="none" stroke="#fff" stroke-width="2.5"/>
      <path d="M22 14 h14 l-2 14 a5 5 0 0 1 -10 0 z" fill="#ffe81a"/>
      <line x1="29" y1="33" x2="29" y2="43" stroke="#fff" stroke-width="2.5"/>
      <line x1="23" y1="44" x2="35" y2="44" stroke="#fff" stroke-width="2.5" stroke-linecap="round"/>
    </svg>
    <p><span class="hl">Tickets only $50 pp online<br>or at Pelican Row Cafe</span><br>Drag shows • Canapés<br>Bubbly on arrival!</p>
  </div>

  <p class="presented">Proudly<br>presented by</p>
  <div class="partner-badges">
    <span class="partner-badge"></span>
    <span class="partner-badge"></span>
  </div>

  <footer class="footer-band">
    <div class="venue">
      <div class="venue-name"><span class="dot"></span>Pelican Row Cafe</div>
      <p class="venue-address">Pelican Row Cafe &amp; Restaurant<br>17 Harbour Lane, Bunbury</p>
    </div>
    <div class="booking">
      <p class="lead">Tickets won't last! Book now at</p>
      <p class="web">www.ticketloom.com.au</p>
      <p class="phone">or phone 9700 2618</p>
    </div>
  </footer>
</main>
</body>
</html>
```